Flyer-Design für nachhaltige Spülbecher aus Keramik
Zielgruppe
Zielgruppe des Flyers sind Zahnärzte. Wir fertigen die ersten nachhaltigen Spülbecher für Praxen aus Keramik.
Aufgabenstellung
Der Flyer soll einen hochwertigen und exklusiven Eindruck hinterlassen.
Auf dem Flyer sollte das Logo, Kontaktmöglichkeiten, Anschrift, 1-2 Bilder des Produktes und ein kleiner Text bezüglich Nachhaltigkeit vorhanden sein. Die aktuell hochgeladenen Bilder der Becher sind aktuell noch Platzhalter, es werden in den nächsten Tagen die richtigen Bilder hochgeladen.
WICHTIG: Bitte einen Platzhalter für eine Überschrift und Stichpunkte/Informationen einarbeiten. Leider ist noch nicht Final klar wir diese Lauten soll, daher wird dieser Teil noch von mir noch selbst ergänzt. Danke
Website: www.lindgau-keramik.de

```html
<!DOCTYPE html>
<html lang="de">
<head>
<meta charset="utf-8">
<title>Lindgau Keramik GmbH – Flyer</title>
<link href="https://fonts.googleapis.com/css2?family=Montserrat:wght@400;600&family=Open+Sans:wght@400;600&display=swap" rel="stylesheet">
<style>
  :root {
    --page: #e4e5e7;
    --cover: #2f2f31;
    --ink: #ffffff;
    --ink-soft: #cfcfd1;
    --ink-muted: #9a9a9e;
    --rule: #5a5a5e;
    --cup-blue: #3f6f8c;
    --cup-pink: #b58f8f;
    --cup-white: #e7e6e1;
    --table: #3a3a3d;
  }
  html, body {
    margin: 0;
    width: 870px;
    height: 1200px;
    overflow: hidden;
    background: var(--page);
  }
  .canvas {
    position: relative;
    width: 870px;
    height: 1200px;
  }
  .cover {
    position: absolute;
    left: 55px;
    width: 760px;
    height: 520px;
    background: var(--cover);
    box-shadow: 0 14px 30px rgba(0,0,0,.22);
    overflow: hidden;
  }
  .cover--front { top: 40px; }
  .cover--back { top: 640px; }

  .cover__photo {
    position: absolute;
    inset: 0;
    width: 100%;
    height: 100%;
  }

  .brand {
    position: absolute;
    top: 56px;
    left: 0;
    width: 100%;
    display: flex;
    align-items: center;
    justify-content: center;
    gap: 12px;
    color: var(--ink);
    font-family: "Montserrat", sans-serif;
    font-weight: 400;
    font-size: 22px;
    letter-spacing: .04em;
  }
  .brand__square {
    width: 14px;
    height: 14px;
    border: 2px solid var(--ink);
  }
  .brand--corner {
    top: auto;
    left: auto;
    right: 44px;
    bottom: 44px;
    width: auto;
    font-size: 18px;
  }

  .info {
    position: absolute;
    top: 44px;
    left: 40px;
    width: 640px;
    color: var(--ink-soft);
    font-family: "Open Sans", sans-serif;
  }
  .info__headline {
    margin: 0 0 14px;
    font-family: "Montserrat", sans-serif;
    font-weight: 600;
    font-size: 24px;
    letter-spacing: .02em;
    color: var(--ink);
  }
  .info__text {
    margin: 0 0 16px;
    font-size: 13.5px;
    line-height: 1.6;
    max-width: 560px;
  }
  .info__list {
    margin: 0;
    padding: 14px 0 0;
    list-style: none;
    border-top: 1px solid var(--rule);
    font-size: 13.5px;
    line-height: 1.5;
  }
  .info__item {
    display: flex;
    gap: 10px;
    margin-bottom: 6px;
  }
  .info__item::before {
    content: "";
    width: 6px;
    height: 6px;
    margin-top: 7px;
    background: var(--ink);
    flex: none;
  }

  .contact {
    position: absolute;
    left: 40px;
    bottom: 38px;
    margin: 0;
    padding: 0;
    list-style: none;
    font-family: "Open Sans", sans-serif;
    font-size: 13px;
    line-height: 1.45;
    color: var(--ink-soft);
  }
  .contact__item {
    display: flex;
    align-items: flex-start;
    gap: 9px;
    margin-top: 7px;
  }
  .contact__icon {
    width: 12px;
    height: 12px;
    margin-top: 3px;
    flex: none;
    fill: none;
    stroke: var(--ink);
    stroke-width: 1.6;
  }
  .contact__name {
    color: var(--ink);
    font-weight: 600;
  }
</style>
</head>
<body>
<main class="canvas">

  <section class="cover cover--front">
    <svg class="cover__photo" viewBox="0 0 760 520" preserveAspectRatio="none" role="img" aria-label="Produktfoto: Keramik-Spülbecher in Blau, Rosé und Weiß auf dunklem Untergrund">
      <defs>
        <linearGradient id="cups" x1="0" y1="0" x2="1" y2="0">
          <stop offset="0" stop-color="var(--table)"/>
          <stop offset=".22" stop-color="var(--cup-blue)"/>
          <stop offset=".48" stop-color="var(--cup-pink)"/>
          <stop offset=".75" stop-color="var(--cup-white)"/>
          <stop offset="1" stop-color="#cfd2d4"/>
        </linearGradient>
        <linearGradient id="shade" x1="0" y1="0" x2="0" y2="1">
          <stop offset="0" stop-color="#000" stop-opacity=".25"/>
          <stop offset=".7" stop-color="#000" stop-opacity="0"/>
          <stop offset="1" stop-color="#000" stop-opacity=".45"/>
        </linearGradient>
      </defs>
      <path d="M0 340 L40 318 L90 300 L150 292 L200 262 L235 252 L290 238 L330 224 L370 212 L410 196 L450 160 L490 150 L530 120 L570 100 L610 92 L650 70 L700 58 L760 40 L760 520 L0 520 Z" fill="url(#cups)"/>
      <path d="M0 340 L40 318 L90 300 L150 292 L200 262 L235 252 L290 238 L330 224 L370 212 L410 196 L450 160 L490 150 L530 120 L570 100 L610 92 L650 70 L700 58 L760 40 L760 520 L0 520 Z" fill="url(#shade)"/>
      <path d="M0 340 L40 318 L90 300 L150 292 L200 262 L235 252 L290 238 L330 224 L370 212 L410 196 L450 160 L490 150 L530 120 L570 100 L610 92 L650 70 L700 58 L760 40" fill="none" stroke="var(--ink)" stroke-width="3" stroke-linejoin="round"/>
    </svg>
    <div class="brand">
      <span class="brand__square"></span>
      <span class="brand__name">Lindgau Keramik GmbH</span>
    </div>
  </section>

  <section class="cover cover--back">
    <div class="info">
      <h2 class="info__headline">Platzhalter für Ihre Überschrift</h2>
      <p class="info__text">Unsere Spülbecher aus Keramik sind langlebig, hygienisch und spülmaschinenfest. Ein Becher ersetzt tausende Einwegbecher – für eine nachhaltige Praxis ohne Plastikmüll.</p>
      <ul class="info__list">
        <li class="info__item">Stichpunkt 1 – Information folgt</li>
        <li class="info__item">Stichpunkt 2 – Information folgt</li>
        <li class="info__item">Stichpunkt 3 – Information folgt</li>
      </ul>
    </div>
    <ul class="contact">
      <li class="contact__item">
        <svg class="contact__icon" viewBox="0 0 12 12"><path d="M6 11 C3 7.5 2 6 2 4.3 A4 4 0 0 1 10 4.3 C10 6 9 7.5 6 11 Z"/><circle cx="6" cy="4.3" r="1.3"/></svg>
        <span><span class="contact__name">Lindgau Keramik GmbH</span><br>Talweg 8<br>37412 Lindgau</span>
      </li>
      <li class="contact__item">
        <svg class="contact__icon" viewBox="0 0 12 12"><path d="M2 1.5 L4.3 1.5 L5.2 4 L3.8 5 C4.5 6.6 5.4 7.5 7 8.2 L8 6.8 L10.5 7.7 L10.5 10 C6 10.5 1.5 6 2 1.5 Z"/></svg>
        <span>0151 / 2384610</span>
      </li>
      <li class="contact__item">
        <svg class="contact__icon" viewBox="0 0 12 12"><rect x="1" y="2.5" width="10" height="7"/><path d="M1 2.5 L6 6.5 L11 2.5"/></svg>
        <span>info@lindgau-keramik.de</span>
      </li>
      <li class="contact__item">
        <svg class="contact__icon" viewBox="0 0 12 12"><circle cx="6" cy="6" r="4.8"/><path d="M1.2 6 H10.8 M6 1.2 C3.8 4 3.8 8 6 10.8 M6 1.2 C8.2 4 8.2 8 6 10.8"/></svg>
        <span>www.lindgau-keramik.de</span>
      </li>
    </ul>
    <div class="brand brand--corner">
      <span class="brand__square"></span>
      <span class="brand__name">Lindgau Keramik</span>
    </div>
  </section>

</main>
</body>
</html>
```